Wine Label Design-Crimson Gully Vineyard

Crimson Gully Vineyard is in the Barossa Valley in South Australia. The Barossa is recognized as Australia's premier wine region, producing Australia's icon wines and some " new takes on traditional".
This family owned and operated vineyard grows some exceptionally high quality fruit. Most of the fruit is sold and used for some of Australia's most iconic wines. Small quantities are retained by the owners for some wines with very limited availability. (Wines were previously sold as Pellow Draycott Vineyards Crimson Gully ( Shiraz, Cabernet etc).

The wines will in the future be labeled simply ‘Crimson Gully Vineyard’. The label will launch this new identity for the single family single vineyard and its high quality wines which are a true expression of the vineyard and derive from the Crimson Gully common to this ancient area (800-2000 million years old).
The label should reflect
• Single vineyard, family owned
• vines in very old rock & soils
• High quality & reliability
• Edgy but true, design based thinking (Please note:blue is generally seen as an unacceptable colour for a wine label?? Don’t ask me why)

The wines will be sold mostly direct in Australia ( ie not through retail stores), with limited export to Asia, Scandinavia and Canada.
There are three quality levels and price points in the portfolio
1. Entry level premium for everyday drinking for discriminating drinkers-approx AUD20
2. Super Premium-approx AUD30
3. Limited Release ultlra premium-AUD75-90?
We envisage three variations on the label but with an obvious & common design element. This design element should be able to be used for corporate identification and promotion
The paper stock will be waterproof and self adhesive. Our preference is for designs that engage the user by appealing to both sight and touch. It is preferred that textures be added eg embossing, high build varnish etc-rather than be a facet of the stock itself.
For information on statutory label requirements refer to www.vintnerregistry-example.com . In brief
o Front label need not show any mandatory information. However we would prefer Variety, Barossa Valley, Year and alcohol to be shown on the front label
o Back label should show all mandatories and allow for a bar code

Project Deadline Extended
Reason: I've had a problem with my wireless broadband account and reception has been intermittent to say the least to the extent that I switched off at the weekend. Just going downtown now for a 'polite discussion' with my service provider.

Project Deadline Extended
Reason: I have receiver insufficient designs of quality which we would consider. Too many designs have a "cut and paste" appearance - too few exhibit an original art/design element which truly identifies the product.

Gals & Guys

most of the designs submitted lack punch and originality and are totally unmemorable.
Please-get on Google or whatever enter "Wine Label Designs" and do some research b4 u waste your time and mine. Formulaic cut and paste will not win the day. That's not to say that cut and paste can't work-but it must have some originality, impact and command attention. Please surprise me.

Following on from a question from a designer about who is our competition and what we are looking for I sent the following 
"I don't think I can add anything new. Read the brief and comments again and research wine labels on the web. In 30 minutes you'll get a good idea of the creative edgy designs in the industry. There are a plethora of collections. Our competition-anyone with a label. In 2010 there were over 2400 "producers" in other words 2400 producers with at least one label. In fact there are over 25000 Australian wines and then the numerous imported wines.

Target Market(s)

$20 people who budget everyday but have graduated from drinking 'entry level' wines. These people will likely fit into Cat. (b) in the $30 wine

$30 (a) will not over-compromise on some everyday discretionary expenditure.(b) might buy for special occasions

$70-$90 Professional/successful people with high disposable/discretionary income not particularly worried about recession. wine geeks.

Industry/Entity Type

Retail

Requirements
Must have
• identifiable element across range of wines

```html
<!DOCTYPE html>
<html lang="en">
<head>
<meta charset="utf-8">
<title>Crimson Gully Vineyard – Super Premium Label</title>
<link rel="stylesheet" href="https://fonts.googleapis.com/css2?family=Josefin+Sans:wght@400;600&family=Oswald:wght@400&family=Pinyon+Script&display=swap">
<style>
  :root {
    --page-bg: #ffffff;
    --tier-band: #0d0d0d;
    --tier-text: #ffffff;
    --label-stock: #5e605f;
    --ornament: #6a6c6b;
    --circle-dark: #0b0b0b;
    --circle-mid: #646665;
    --label-ink: #e6e6e6;
    --label-ink-dark: #1a1a1a;
  }
  * { margin: 0; padding: 0; box-sizing: border-box; }
  html, body {
    width: 1200px;
    height: 837px;
    overflow: hidden;
    background: var(--page-bg);
  }
  .canvas {
    position: relative;
    width: 1200px;
    height: 837px;
  }
  .tier-band {
    position: absolute;
    left: 0;
    top: 55px;
    width: 240px;
    height: 19px;
    background: var(--tier-band);
    color: var(--tier-text);
    font-family: "Josefin Sans", sans-serif;
    font-weight: 600;
    font-size: 12px;
    letter-spacing: 3px;
    line-height: 21px;
    padding-left: 20px;
  }
  .label {
    position: absolute;
    top: 363px;
    width: 117px;
    height: 277px;
  }
  .label--rose { left: 358px; }
  .label--white { left: 528px; }
  .label--red { left: 699px; }
  .label svg { display: block; width: 117px; height: 277px; }
  .stock { fill: var(--label-stock); }
  .ornament { fill: var(--ornament); }
  .circle-dark { fill: var(--circle-dark); }
  .circle-mid { fill: var(--circle-mid); }
  .variety {
    font-family: "Josefin Sans", sans-serif;
    font-size: 6.6px;
    letter-spacing: 1.2px;
    fill: var(--label-ink);
  }
  .brand-name {
    font-family: "Oswald", sans-serif;
    font-size: 10.5px;
    letter-spacing: 1.6px;
    fill: var(--label-ink);
  }
  .origin {
    font-family: "Pinyon Script", cursive;
    font-size: 8.5px;
    fill: var(--label-ink);
  }
  .vintage {
    font-family: "Josefin Sans", sans-serif;
    font-size: 6.4px;
    letter-spacing: 1.2px;
    fill: var(--label-ink);
  }
  .statutory {
    font-family: "Josefin Sans", sans-serif;
    font-size: 5px;
    fill: var(--label-ink-dark);
  }
</style>
</head>
<body>
<main class="canvas">
  <div class="tier-band">SUPER PREMIUM</div>

  <div class="label label--rose">
    <svg viewBox="0 0 117 277" aria-label="Crimson Gully Shiraz front label">
      <rect class="stock" width="117" height="277"/>
      <rect class="ornament" x="4" y="40" width="109" height="200" role="img" aria-label="fine-line mandala ornament behind the circles" opacity="0.55"/>
      <circle class="circle-dark" cx="58.5" cy="50" r="46"/>
      <circle class="circle-dark" cx="58.5" cy="229" r="46"/>
      <circle class="circle-mid" cx="58.5" cy="140" r="46"/>
      <text class="variety" x="58.5" y="58" text-anchor="middle">SHIRAZ</text>
      <text class="variety" x="58.5" y="68" text-anchor="middle">BARROSA VALLEY</text>
      <text class="brand-name" x="58.5" y="138" text-anchor="middle">CRIMSON</text>
      <text class="brand-name" x="58.5" y="152" text-anchor="middle">GULLY</text>
      <text class="origin" x="58.5" y="224" text-anchor="middle">Wine Of Australia</text>
      <text class="vintage" x="58.5" y="235" text-anchor="middle">2012</text>
      <text class="statutory" x="5" y="269">13.5%vol</text>
      <text class="statutory" x="112" y="269" text-anchor="end">750ml</text>
    </svg>
  </div>

  <div class="label label--white">
    <svg viewBox="0 0 117 277" aria-label="Crimson Gully Shiraz front label">
      <rect class="stock" width="117" height="277"/>
      <rect class="ornament" x="4" y="40" width="109" height="200" role="img" aria-label="fine-line mandala ornament behind the circles" opacity="0.55"/>
      <circle class="circle-dark" cx="58.5" cy="50" r="46"/>
      <circle class="circle-dark" cx="58.5" cy="229" r="46"/>
      <circle class="circle-mid" cx="58.5" cy="140" r="46"/>
      <text class="variety" x="58.5" y="58" text-anchor="middle">SHIRAZ</text>
      <text class="variety" x="58.5" y="68" text-anchor="middle">BARROSA VALLEY</text>
      <text class="brand-name" x="58.5" y="138" text-anchor="middle">CRIMSON</text>
      <text class="brand-name" x="58.5" y="152" text-anchor="middle">GULLY</text>
      <text class="origin" x="58.5" y="224" text-anchor="middle">Wine Of Australia</text>
      <text class="vintage" x="58.5" y="235" text-anchor="middle">2012</text>
      <text class="statutory" x="5" y="269">13.5%vol</text>
      <text class="statutory" x="112" y="269" text-anchor="end">750ml</text>
    </svg>
  </div>

  <div class="label label--red">
    <svg viewBox="0 0 117 277" aria-label="Crimson Gully Shiraz front label">
      <rect class="stock" width="117" height="277"/>
      <rect class="ornament" x="4" y="40" width="109" height="200" role="img" aria-label="fine-line mandala ornament behind the circles" opacity="0.55"/>
      <circle class="circle-dark" cx="58.5" cy="50" r="46"/>
      <circle class="circle-dark" cx="58.5" cy="229" r="46"/>
      <circle class="circle-mid" cx="58.5" cy="140" r="46"/>
      <text class="variety" x="58.5" y="58" text-anchor="middle">SHIRAZ</text>
      <text class="variety" x="58.5" y="68" text-anchor="middle">BARROSA VALLEY</text>
      <text class="brand-name" x="58.5" y="138" text-anchor="middle">CRIMSON</text>
      <text class="brand-name" x="58.5" y="152" text-anchor="middle">GULLY</text>
      <text class="origin" x="58.5" y="224" text-anchor="middle">Wine Of Australia</text>
      <text class="vintage" x="58.5" y="235" text-anchor="middle">2012</text>
      <text class="statutory" x="5" y="269">13.5%vol</text>
      <text class="statutory" x="112" y="269" text-anchor="end">750ml</text>
    </svg>
  </div>
</main>
</body>
</html>
```